Wealth Management Business Card

We are a professional services consulting firm that specializes in high net worth individuals over $25,000,000, executives C-suite and above, closely held businesses owners, family offices and highly compensated employees.

Our focus is on risk mitigation and tax efficient strategies. Our clients take their risk on themselves and have a proven track record generating wealth. Our directive is to preserve and protect the wealth they’ve already created.

Our company Harbridge Advisory is geared around five directives of asset protection:
1) Legal Structuring
2) Leverage & Financing
3) Risk Management - Asset Protection & Insurance, Trustee Work
4) Asset Management & Investing - Under www.qelvantcapital.com
5) Tax Efficient Strategies

Our Company Mark is a Pentagon with a key in the middle. A pentagon is the most efficient defensive structure. Each point of a pentagon is equal distance front every point . Each side provides support to another and works together, which is the key to our clients success.

Our key colors are blue, black and silver.

We ‘re located in the Pacific Northwest with bi coastal and international clients. We have fewer, higher net worth clients and provide exceptional customer service. We do not do social media.

website is www.harbridgepath.com

Target Market(s)

High End Clients

Contact Information for Business Card

extra thick

Font styles to use
Serif

Requirements
Must have
• Metalic foil for lettering.
Black Background on one side
White Background on the other
Horizontal Format Only
No Rounded corners
Not Marketing sales information on the card.
Nice to have
• imprinted texture on the card
Should not have
• lots of color

```html
<!DOCTYPE html>
<html lang="en">
<head>
<meta charset="utf-8">
<title>Harbridge Advisory — Business Card</title>
<link rel="stylesheet" href="https://fonts.googleapis.com/css2?family=Cinzel:wght@400;600&family=Tinos:ital@0;1&display=swap">
<style>
  :root {
    --backdrop: #2a2a2a;
    --card: #1b1b1c;
    --card-edge: #111112;
    --silver: #e6e6e6;
    --silver-soft: #cfcfcf;
    --deep-mark: #2c2c2e;
    --blue: #1f8fd6;
    --blue-deep: #0d4f9a;
  }
  * { margin: 0; padding: 0; box-sizing: border-box; }
  html, body { width: 1200px; height: 1138px; overflow: hidden; }
  body { background: var(--backdrop); position: relative; font-family: "Tinos", "Times New Roman", serif; color: var(--silver); }

  .card {
    position: absolute;
    left: 274px;
    width: 622px;
    height: 376px;
    background: var(--card);
    border: 1px solid var(--card-edge);
  }
  .card--front { top: 186px; }
  .card--back { top: 606px; }

  .services {
    position: absolute;
    left: 0; right: 0;
    text-align: center;
    font-size: 13.6px;
    line-height: 15.5px;
    letter-spacing: 0.1px;
    color: var(--silver-soft);
  }
  .services .sep { color: var(--blue); padding: 0 6px; }
  .card--back .services .sep { color: var(--silver-soft); }
  .card--front .services { top: 322px; }
  .card--back .services { top: 323px; }

  .front-name {
    position: absolute;
    top: 118px; left: 0; right: 0;
    text-align: center;
    font-family: "Cinzel", "Times New Roman", serif;
    font-weight: 600;
    font-size: 40px;
    letter-spacing: 4px;
    color: var(--deep-mark);
  }

  .brand {
    position: absolute;
    top: 72px; left: 0; right: 0;
    display: flex;
    justify-content: center;
    align-items: center;
    gap: 16px;
  }
  .brand__dot { width: 18px; height: 18px; border-radius: 50%; background: var(--blue); }
  .brand__name {
    font-family: "Cinzel", "Times New Roman", serif;
    font-weight: 600;
    font-size: 38px;
    letter-spacing: 2px;
    color: var(--silver);
  }

  .person { position: absolute; top: 164px; left: 0; right: 0; text-align: center; }
  .person__name {
    font-family: "Cinzel", "Times New Roman", serif;
    font-weight: 600;
    font-size: 24px;
    letter-spacing: 0.5px;
    color: var(--silver);
    line-height: 28px;
  }
  .person__title {
    display: inline-flex; align-items: center; gap: 14px;
    font-style: italic; font-size: 16px; color: var(--silver-soft);
  }
  .person__title::before, .person__title::after {
    content: ""; width: 36px; height: 1px; background: var(--blue-deep);
  }

  .contacts {
    position: absolute; top: 244px; left: 0; right: 0;
    display: flex; justify-content: center; align-items: center; gap: 12px;
    font-size: 16px; color: var(--silver);
  }
  .contact { display: inline-flex; align-items: center; gap: 9px; }
  .contact svg { width: 20px; height: 20px; }
  .address {
    position: absolute; top: 271px; left: 0; right: 0;
    text-align: center; font-size: 16px; color: var(--silver);
  }
  .rule {
    position: absolute; top: 308px; left: 0; right: 0; height: 2px;
    background: linear-gradient(90deg, var(--blue-deep) 0%, var(--blue-deep) 50%, var(--blue) 50%, var(--blue) 100%);
  }
</style>
</head>
<body>

  <section class="card card--front" aria-label="Card front">
    <div class="front-name">HARBRIDGE ADVISORY</div>
    <p class="services">
      LEGAL STRUCTURING<span class="sep">|</span>LEVERAGE &amp; FINANCING<span class="sep">|</span>RISK MANAGEMENT<br>
      ASSET MANAGEMENT &amp; INVESTING<span class="sep">|</span>TAX EFFICIENT STRATEGIES
    </p>
  </section>

  <section class="card card--back" aria-label="Card back">
    <div class="brand">
      <span class="brand__dot"></span>
      <span class="brand__name">HARBRIDGE ADVISORY</span>
    </div>

    <div class="person">
      <div class="person__name">CORWIN ASHDALE</div>
      <div class="person__title">Financial Strategist</div>
    </div>

    <div class="contacts">
      <span class="contact">
        <svg viewBox="0 0 20 20" aria-hidden="true"><circle cx="10" cy="10" r="10" fill="#1f8fd6"/><path d="M7 5.5l1.6 2.4-1 1a6 6 0 0 0 3.5 3.5l1-1 2.4 1.6-.8 1.5c-3.8.2-7.9-3.9-7.7-7.7z" fill="#fff"/></svg>
        (503) 555-0147
      </span>
      <span class="contact">
        <svg viewBox="0 0 20 20" aria-hidden="true"><circle cx="10" cy="10" r="10" fill="#1f8fd6"/><rect x="5" y="6.5" width="10" height="7" fill="none" stroke="#fff" stroke-width="1.3"/><path d="M5 6.5l5 4 5-4" fill="none" stroke="#fff" stroke-width="1.3"/></svg>
        info@harbridgepath.com
      </span>
      <span class="contact">
        <svg viewBox="0 0 20 20" aria-hidden="true"><circle cx="10" cy="10" r="10" fill="#1f8fd6"/><circle cx="10" cy="10" r="5" fill="none" stroke="#fff" stroke-width="1.2"/><ellipse cx="10" cy="10" rx="2.2" ry="5" fill="none" stroke="#fff" stroke-width="1.1"/><path d="M5 10h10" stroke="#fff" stroke-width="1.1"/></svg>
        www.harbridgepath.com
      </span>
    </div>
    <p class="address">418 Alder Crest Ave, Suite 310, Westbrook, OR 97199</p>

    <div class="rule"></div>

    <p class="services">
      LEGAL STRUCTURING<span class="sep">|</span>LEVERAGE &amp; FINANCING<span class="sep">|</span>RISK MANAGEMENT<br>
      ASSET MANAGEMENT &amp; INVESTING<span class="sep">|</span>TAX EFFICIENT STRATEGIES
    </p>
  </section>

</body>
</html>
```